Professional New Resume for personal/ company

Specialist in construction law, disputes and quantity surveying. Looking for a new fresh CV to appeal to the middle east (UAE) market.

Target Market(s)

employers, clients, lawyers, expert witnesses

Industry/Entity Type

Construction law, quantity surveying, dispute resolution.

```html
<!DOCTYPE html>
<html lang="en">
<head>
<meta charset="utf-8">
<title>Callum J Hartley – Curriculum Vitae</title>
<link rel="stylesheet" href="https://fonts.googleapis.com/css2?family=Poppins:wght@400;500;600;700&display=swap">
<style>
  :root{
    --backdrop:#ababab;
    --paper:#ffffff;
    --navy:#0b5cb5;
    --sky:#61ace3;
    --ring:#0d5fc0;
    --ink:#2b2b2b;
    --muted:#555a60;
    --rule:#6b6b6b;
  }
  *{box-sizing:border-box;margin:0;padding:0}
  html,body{width:1200px;height:870px;overflow:hidden}
  body{background:var(--backdrop);font-family:"Poppins",sans-serif;color:var(--ink);position:relative}

  .page{position:absolute;top:90px;width:490px;height:690px;background:var(--paper);overflow:hidden}
  .page--front{left:100px}
  .page--back{left:612px}
  .sidebar-shape{position:absolute;left:0;top:0;width:490px;height:690px}

  /* shared */
  .pill{position:absolute;z-index:2;height:18px;border-radius:9px;background:var(--navy);color:#fff;
        font-weight:600;font-size:9.5px;line-height:18px;padding-left:10px;white-space:nowrap}
  .card{position:absolute;z-index:1;background:var(--paper);border-radius:3px}
  .bullets{list-style:none;font-size:6.9px;line-height:8.6px;color:var(--ink)}
  .bullets li{position:relative;padding-left:10px;margin-bottom:6px}
  .bullets li::before{content:"";position:absolute;left:1px;top:3px;width:2.6px;height:2.6px;border-radius:50%;background:var(--navy)}

  /* front page */
  .brand{position:absolute;left:362px;top:22px;display:flex;align-items:center;gap:5px;
         font-weight:500;font-size:16px;letter-spacing:3px;color:var(--navy)}
  .brand__mark{width:8px;height:8px;background:var(--navy)}
  .portrait{position:absolute;left:30px;top:40px;width:160px;height:160px}
  .name{position:absolute;left:226px;top:80px;font-weight:700;font-size:23.5px;letter-spacing:0;color:var(--navy);line-height:28px;white-space:nowrap}
  .credentials{position:absolute;left:226px;top:113px;width:250px;font-size:13.5px;line-height:19px;color:var(--muted)}
  .overview{position:absolute;left:226px;top:222px;width:242px;font-size:6.9px;line-height:9.6px;text-align:justify}

  .contact{list-style:none;font-size:6.8px;line-height:8.4px}
  .contact li{display:flex;gap:7px;margin-bottom:3px}
  .contact svg{flex:none;width:7px;height:7px;margin-top:1px;fill:var(--navy)}

  /* timeline entries */
  .timeline{position:absolute;left:229px;border-left:.8px solid var(--rule)}
  .entry{position:relative;display:grid;grid-template-columns:59px 1fr;padding-left:16px;
         font-size:6.9px;line-height:9.1px}
  .entry::before{content:"";position:absolute;left:-2.6px;top:2px;width:4.4px;height:4.4px;border-radius:50%;background:#444}
  .entry dt{color:var(--ink)}
  .entry dd{color:var(--ink)}

  /* back page */
  .training{font-size:6.9px;line-height:8.2px}
  .training li{position:relative;list-style:none;padding-left:10px}
  .training li::before{content:"";position:absolute;left:1px;top:3px;width:2.6px;height:2.6px;border-radius:50%;background:var(--navy)}
  .training .when{color:var(--navy);font-weight:500}
  .training .sub{padding-left:12px}
  .training .gap{margin-top:8px}
</style>
</head>
<body>

<!-- FRONT PAGE -->
<section class="page page--front">
  <svg class="sidebar-shape" viewBox="0 0 490 690" aria-hidden="true">
    <polygon points="0,0 34,0 208,300 208,690 0,690" fill="var(--sky)"/>
  </svg>

  <div class="brand"><span class="brand__mark"></span>VERALEX</div>

  <svg class="portrait" viewBox="0 0 160 160">
    <path d="M20 80 A60 60 0 1 1 150 108" fill="none" stroke="var(--ring)" stroke-width="7"/>
    <circle cx="80" cy="80" r="64" fill="#fff"/>
    <defs>
      <linearGradient id="portraitTone" x1="0" y1="0" x2="0" y2="1">
        <stop offset="0" stop-color="#e9ecef"/>
        <stop offset="0.55" stop-color="#c9b4a4"/>
        <stop offset="1" stop-color="#2d3240"/>
      </linearGradient>
    </defs>
    <circle cx="80" cy="80" r="59" fill="url(#portraitTone)" role="img" aria-label="Portrait photograph of Callum J Hartley in a pinstripe suit"/>
  </svg>

  <h1 class="name">CALLUM J HARTLEY</h1>
  <p class="credentials">BSc (Hons), Dip. Adj, LLM, FCGArb,<br>FRSCS, MCSCES, MCGB</p>

  <div class="pill" style="left:226px;top:195px;width:242px">Overview</div>
  <p class="overview">Adjudicator, Chartered Quantity Surveyor and Chartered Construction Manager with experience in Private Practice, Development and Main Contracting industry. Claims, contract and dispute resolution (adjudication) services (as adjudicator or party representative) provided in Scotland, England and Wales. Qualifications include:- a BSc (Hons) in Quantity Surveying, LLM Masters of Law (Construction Law), Fellow of The Chartered Guild of Arbitrators (FCGArb), Fellow of The Royal Society of Chartered Surveyors (FRSCS); Member of The Chartered Society of Civil Engineering Surveyors (MCSCES) and a Professional Member of The Chartered Guild of Building (MCGB). Experience includes involvement in a large and complex international arbitration. Experienced in JCT, SBCC, NEC3/4 and FIDIC.</p>

  <div class="pill" style="left:226px;top:394px;width:242px">Experience</div>
  <dl class="timeline" style="top:424px;height:256px">
    <div class="entry"><dt>Project:<br>Value:<br>For:<br>Date:<br>Services:</dt>
      <dd>Confidential<br>£12bn claim &amp; counter-claim<br>Parties to an International Arbitration<br>December 2020 to Current<br>Tribunal secretary to assist the Arbitral Tribunal (Chairman (Martin Greave KC) and two co-arbitrators (Sir Edwin Marlow and Peter Dunsford OBE, KC).</dd></div>
    <div class="entry" style="margin-top:12px"><dt>Project:<br>Value:<br>For:<br><br>Date:<br>Services:</dt>
      <dd>Various<br>Various<br>Adjudicator in Construction Disputes, nominated by Panel Adjudicators UK.<br>October 2021 to current.<br>Adjudicator</dd></div>
    <div class="entry" style="margin-top:12px"><dt>Project:<br>Value:<br>For:<br>Date:<br>Services:</dt>
      <dd>Flat Development, Edinburgh<br>£24,000<br>Referring Party (Contractor)<br>December 2020<br>Representative for Referring Party</dd></div>
    <div class="entry" style="margin-top:12px"><dt>Project:<br>Value:<br>For:<br>Date:<br>Services:</dt>
      <dd>Supermarkets (various)<br>Various<br>Referring Party (Subcontractor)<br>January 2019<br>Representative for Referring Party</dd></div>
  </dl>

  <div class="pill" style="left:20px;top:239px;width:112px">Contact Info.</div>
  <div class="card" style="left:28px;top:250px;width:155px;height:65px;padding:11px 8px 0 9px">
    <ul class="contact">
      <li><svg viewBox="0 0 10 10"><path d="M2 0.5 3.6 2.8 2.6 3.9C3.3 5.4 4.6 6.7 6.1 7.4L7.2 6.4 9.5 8 8.2 9.5C4.3 9.3 0.7 5.7 0.5 1.8Z"/></svg>+44 (0)7000 123 456</li>
      <li><svg viewBox="0 0 10 10"><path d="M0.5 2H9.5V8H0.5ZM1.2 2.6 5 5.5 8.8 2.6"/></svg>callum@veralex.example</li>
      <li><svg viewBox="0 0 10 10"><path d="M5 0.4A3.4 3.4 0 0 1 8.4 3.8C8.4 6.2 5 9.6 5 9.6S1.6 6.2 1.6 3.8A3.4 3.4 0 0 1 5 0.4ZM5 2.6A1.2 1.2 0 1 0 5 5 1.2 1.2 0 1 0 5 2.6Z"/></svg>2nd Floor, 18 Harrow Crescent, Glasgow, Scotland, United Kingdom, G1 7XZ</li>
    </ul>
  </div>

  <div class="pill" style="left:20px;top:351px;width:150px">Qualifications</div>
  <div class="card" style="left:28px;top:362px;width:155px;height:106px;padding:12px 8px 0 8px">
    <ul class="bullets">
      <li>BSc (Hons) Quantity Surveying (Clydeside Technical University) (part-time)</li>
      <li style="margin-top:9px">LLM Masters of Law (Construction Law) (University of Kelvinmouth) (with Merit)</li>
      <li style="margin-top:9px">Diploma in Adjudication (CGArb)</li>
    </ul>
  </div>

  <div class="pill" style="left:20px;top:505px;width:150px">Memberships</div>
  <div class="card" style="left:28px;top:516px;width:155px;height:147px;padding:11px 8px 0 8px">
    <ul class="bullets">
      <li>Fellow of The Chartered Guild of Arbitrators</li>
      <li style="margin-top:8px">Fellow of The Royal Society of Chartered Surveyors</li>
      <li style="margin-top:8px">Member of The Chartered Society of Civil Engineering Surveyors</li>
      <li style="margin-top:8px">Member of The Chartered Guild of Building</li>
      <li style="margin-top:8px">Adjudicator &amp; Panel Member – PAUK (Panel Adjudicators UK)</li>
    </ul>
  </div>
</section>

<!-- BACK PAGE -->
<section class="page page--back">
  <svg class="sidebar-shape" viewBox="0 0 490 690" aria-hidden="true">
    <rect x="0" y="0" width="208" height="690" fill="var(--sky)"/>
  </svg>

  <div class="pill" style="left:20px;top:22px;width:152px">Training and Courses</div>
  <div class="card" style="left:27px;top:24px;width:155px;height:336px;padding:24px 6px 0 7px">
    <ul class="training">
      <li><span class="when">October 2021</span><br>The Royal Society of Chartered Surveyors, APC Assessor Training</li>
      <li><span class="when">October 2021</span><br>The Chartered Guild of Arbitrators<br>Diploma in International Arbitration (Module 1)</li>
      <li><span class="when">December 2019</span><br>The Royal Society of Chartered Surveyors; APC Counsellor Training</li>
      <li><span class="when">2017 to 2019</span><br>The Chartered Guild of Arbitrators<br>Construction Adjudication Pathway
        <div class="sub">Module 1 – Law of Obligations and Civil Evidence</div>
        <div class="sub">Module 2 – Construction Adjudication</div>
        <div class="sub">Module 3 – Construction Adjudication</div>
        <div class="sub">Module 4 – Decision Writing</div></li>
      <li><span class="when">2017 to 2019</span><br>The University of Kelvinmouth<br>Masters of Law, Construction Law (with Merit)
        <div class="gap">Legal Research<br>Law of the Construction Industry<br>Law and Practice of Construction Management<br>Legal Process and the Law of Contracts and Other Obligations<br>Dispute Resolution<br>Arbitration Law</div></li>
    </ul>
  </div>

  <div class="pill" style="left:20px;top:379px;width:152px">Employment History</div>
  <div class="card" style="left:27px;top:382px;width:155px;height:285px;padding:20px 6px 0 7px">
    <ul class="bullets">
      <li>December 2018 to current<br>Director of VERALEX Ltd</li>
      <li style="margin-top:9px">January 2017 to November 2018 Cowan and Hale Ltd (Contract &amp; Dispute Consultant)</li>
      <li style="margin-top:9px">November 2015 to December 2016 Ashby Building Projects Ltd (Senior Quantity Surveyor)</li>
      <li style="margin-top:9px">May 2015 to November 2015 Marlowe &amp; Stanton Retirement Lifestyles Ltd</li>
      <li style="margin-top:9px">February 2014 to May 2015 DRK (Glasgow) Ltd – Contract Surveyor</li>
      <li style="margin-top:9px">February 2013 to February 2014 Tennant &amp; Forbes Ltd – Quantity Surveyor</li>
      <li style="margin-top:9px">March 2012 to February 2013 Oakfield (Glasgow) Ltd – Quantity Surveyor</li>
      <li style="margin-top:9px">July 2006 to March 2012 Brisk Group (Carron &amp; Bell) – Cost Consultant</li>
    </ul>
  </div>

  <div class="pill" style="left:224px;top:20px;width:245px">Experience Cont.</div>
  <dl class="timeline" style="top:50px;height:628px">
    <div class="entry"><dt>Project:<br>Value:<br>For:<br><br>Date:<br>Services:</dt>
      <dd>Confidential<br>£2bn<br>Brantwell plc (consulting for Corvane International)<br>February 2019 to Current<br>Conclude and implement compensation event quotations under NEC3/4 contracts. Commercial management services, procurement advice, dispute avoidance.</dd></div>
    <div class="entry" style="margin-top:16px"><dt>Project:<br><br>Value:<br>For:<br>Date:<br>Services:</dt>
      <dd>Northlake Infrastructure, Data Centre Project, Sweden<br>Undisclosed<br>Consulting for Corvane International<br>January to February 2019<br>Review of Memorandum of Understanding, Northlake standard services contract, alignment of contracts</dd></div>
    <div class="entry" style="margin-top:16px"><dt>Project:<br>For:<br>Date:<br>Services:</dt>
      <dd>The Lancet Tower, London<br>Vitrafacade<br>2018<br>Contract and commercial management of JCT D&amp;B contract; dispute avoidance; claim preparation for loss and/ or expense; legal opinion instructed from leading QC of 12 Fleetgate Chambers regarding liquidated damages clause within contract.</dd></div>
    <div class="entry" style="margin-top:16px"><dt>Project:<br>Value:<br>For:<br>Date:<br>Services:</dt>
      <dd>Energy for Waste, Kidderminster<br>c£5m<br>Ridgemoor Ltd<br>2017<br>Commercial management prior to adjudication, preparation of loss and/ or expense claim; assisted with drafting the Referral and subsequent adjudication documents, attended hearing and assisted with representation of the Client.</dd></div>
    <div class="entry" style="margin-top:16px"><dt>Project:<br>Value:<br>For:<br>Date:<br>Services:</dt>
      <dd>Metro Rail London, Lift Schemes<br>c£5m<br>Halden Engineering Services Ltd<br>2018<br>Commercial and contract management of NEC3 contract.</dd></div>
    <div class="entry" style="margin-top:16px"><dt>Project:<br>Value:<br>For:<br>Date:<br>Services:</dt>
      <dd>Fenwick Motors, Car Garage, Glasgow<br>c£6m<br>Ashby Building Projects Ltd<br>2016<br>Commercial and contract management; preparation of claim for damages due to wrongful termination of building contract, assisted Lorimer Kent with the quantum calculations and support during the adjudication and assisted with the drafting and reviewing of adjudication submissions.</dd></div>
  </dl>
</section>

</body>
</html>
```